Website design for Harbor Bolts. ( Lock company)

Harbor Bolts is a New York Based Company that manufactures a variety of high quality Locks which sell worldwide.

Our website: We need a 'face' on the Internet , a website that tells you who we are and what we do - 'An Identity'.

it is not an eCommerce website . the website is to show customers and potential distributers who we are and what we manufacture ( so they come away with a great impression of our company and our products) see www.quarrymillwheel.com

First glance impression: We are Professional; are locks are strong,and reliable. and we are ready to compete with other major Lock companies

Content: for starters the site will contain general information and background about our company (our story), were to buy our products, contact information, and display images of our Locks (and of course all the classic links including to all the legal and technical information). as time goes on we will add more features to the website i.e. Products, Videos blogs etc.

although at first there will not be that much content on the website - it should not look empty (it should be simple and clear but not empty) it should look and feel like a full fledged professional website (not a template)

Inspiration: here are a few sites which have the feel we are looking for:

General tone - quarrymillwheel.com bantrell.com (black is good - But not a must )

Simplicity, clarity - coolvantix.com hearthmate.com

the widescreen Image look - http://www.layoutgarden.com/demo/81952.html

we are considering perhaps having wide HQ images of Lion(s) in the background (but without the felling that it is a zoo or safari website) - it is not a must, its just an idea .

perhaps (if you find it looks good ) use a bit of that metal or chrome look to give it it a strong smooth feel (however it should not look like a dark prison)

We do not currently have a Logo ( if you feel you can design one that fits the above company description - we would love to see if it can work for us) We can talk about additional funds for the logo during this project.

Our working slogan is : Harbor Bolts - "Keeper of the Gate"

for your convenience we have attached a few images of the type of locks we sell

We are looking to collaborate with you throughout the project. We have ideas and visions we want implemented and we will help you along the way. So we can create the perfect website.

Thank you.

```html
<!DOCTYPE html>
<html lang="en">
<head>
<meta charset="utf-8">
<title>Harbor Bolts – Keeper of the Gate</title>
<link href="https://fonts.googleapis.com/css2?family=Michroma&family=Play:wght@400;700&display=swap" rel="stylesheet">
<style>
:root{
  --bg:#1c1c1c;
  --bg-dark:#0d0d0d;
  --bg-hero:#161616;
  --bg-footer:#151515;
  --gold:#c6a55c;
  --gold-deep:#a8894a;
  --gold-card:#ad9158;
  --white:#ffffff;
  --muted:#7c7c7c;
  --line:#2c2c2c;
}
*{margin:0;padding:0;box-sizing:border-box}
html,body{width:755px;height:1200px;overflow:hidden}
body{background:var(--bg);color:var(--white);font-family:"Play",sans-serif;position:relative}
.head-font{font-family:"Michroma",sans-serif}
.abs{position:absolute}

/* header */
.site-header{position:absolute;left:0;top:0;width:755px;height:34px;background:var(--bg-dark);border-bottom:1px solid #222}
.brand{position:absolute;left:93px;top:9px;display:flex;align-items:center;gap:6px;font-family:"Michroma",sans-serif;font-size:12px;color:var(--gold);letter-spacing:.5px}
.brand-mark{width:14px;height:14px;border-radius:50%;background:var(--gold)}
.main-nav{position:absolute;right:50px;top:13px;display:flex;gap:20px;font-family:"Michroma",sans-serif;font-size:7px;color:var(--gold)}
.main-nav .active{color:var(--white);position:relative}
.main-nav .active::after{content:"";position:absolute;left:-3px;right:-3px;top:20px;height:2px;background:var(--white)}

/* hero */
.hero{position:absolute;left:0;top:35px;width:755px;height:298px;background:radial-gradient(ellipse at 45% 40%,#262626 0%,var(--bg-hero) 70%);border-bottom:1px solid #252525}
.hero-photo{position:absolute;left:92px;top:55px;width:235px;height:210px;border-radius:40% 45% 30% 40%;background:radial-gradient(circle at 45% 40%,#f3d68e 0%,#c59a3e 45%,rgba(90,65,20,.0) 72%)}
.tag{position:absolute;background:linear-gradient(#fff,#d6d6d6);color:#111;font-family:"Michroma",sans-serif;font-size:7px;padding:4px 7px;border-radius:2px}
.hero-title{position:absolute;left:387px;top:73px;font-family:"Michroma",sans-serif;font-weight:400;line-height:1}
.hero-title .l1{display:block;font-size:25px;color:var(--gold);letter-spacing:1px}
.hero-title .l2{display:block;font-size:17px;color:var(--white);margin-top:8px;letter-spacing:1px}
.hero-points{position:absolute;left:388px;top:140px;list-style:none;font-family:"Michroma",sans-serif;font-size:7px;color:var(--gold);line-height:17.5px}
.hero-points li::before{content:"";display:inline-block;width:4px;height:4px;border-radius:50%;background:var(--white);margin-right:6px;vertical-align:1px}
.btn-light{position:absolute;left:387px;top:197px;width:73px;height:21px;background:linear-gradient(#fff,#d4d4d4);color:#111;font-family:"Michroma",sans-serif;font-size:6.5px;display:flex;align-items:center;justify-content:center;border-radius:2px}
.slider-tabs{position:absolute;left:251px;top:276px;display:flex;gap:4px}
.slider-tabs span{width:48px;border-top:3px solid #e8e8e8;text-align:center;font-size:7px;padding-top:5px;color:#ddd;font-family:"Michroma",sans-serif}
.slider-tabs .on{border-color:var(--gold);color:var(--gold)}

/* feature cards */
.card{position:absolute;top:377px;height:212px}
.card-photo{background:#0b0b0b}
.card-photo .img{position:absolute;left:35px;top:20px;width:88px;height:130px;border-radius:8px}
.card-frame{position:absolute;left:7px;top:7px;right:7px;bottom:7px;border:2px solid var(--gold-deep)}
.card-label{position:absolute;left:0;right:0;top:183px;text-align:center;font-family:"Michroma",sans-serif;font-size:10px;color:var(--gold);line-height:1}
.card-label small{display:block;font-size:5.5px;margin-top:3px}
.card-promo{left:256px;width:244px;background:var(--gold-card)}
.card-promo .card-frame{border-color:#c5aa72}
.card-promo h2{position:absolute;left:0;right:0;top:43px;text-align:center;font-family:"Michroma",sans-serif;font-size:12px;font-weight:400}
.card-promo p{position:absolute;left:30px;right:30px;top:64px;text-align:center;font-size:9.5px;line-height:12px}
.btn-dark{position:absolute;left:86px;top:150px;width:72px;height:20px;background:#151515;color:var(--gold);font-family:"Michroma",sans-serif;font-size:6px;display:flex;align-items:center;justify-content:center;border-radius:2px}
.card-promo .faint{position:absolute;left:0;right:0;top:186px;text-align:center;font-family:"Michroma",sans-serif;font-size:9px;color:#bca06a;line-height:1}
.card-promo .faint small{display:block;font-size:5px;margin-top:2px}

.divider{position:absolute;left:91px;top:627px;width:574px;height:1px;background:var(--line)}
.section-title{position:absolute;left:0;width:755px;top:657px;text-align:center;font-family:"Michroma",sans-serif;font-size:12px;letter-spacing:.5px}

/* news */
.news{position:absolute;top:691px;width:180px}
.news .img{height:124px}
.news h3{margin-top:13px;font-family:"Michroma",sans-serif;font-weight:400;font-size:10px;color:var(--gold);letter-spacing:.3px}
.news p{margin-top:8px;font-size:8px;line-height:9.8px}
.news a{display:block;margin-top:8px;font-size:7px;font-weight:700;color:var(--gold);text-decoration:none;letter-spacing:.5px}

/* footer */
.site-footer{position:absolute;left:0;top:934px;width:755px;height:266px;background:var(--bg-footer)}
.f-col{position:absolute;top:44px}
.f-col h4{font-family:"Michroma",sans-serif;font-weight:400;font-size:7px;padding-bottom:4px;border-bottom:2px solid var(--gold);display:inline-block}
.f-col ul{list-style:none;margin-top:9px;font-size:6px;color:var(--muted);line-height:14.6px}
.f-col .hl{color:var(--gold)}
.social{display:flex;gap:8px;margin-top:9px}
.social span{width:9px;height:9px;border-radius:50%;background:var(--gold)}
.f-info{font-size:6.5px;color:var(--gold);line-height:11px;margin-top:8px}
.f-col h4.gap{margin-top:18px}
.bottom-bar{position:absolute;left:91px;top:236px;width:574px;border-top:1px solid var(--line);padding-top:10px;display:flex;justify-content:space-between;font-size:6px}
.bottom-nav{display:flex;gap:14px;font-family:"Michroma",sans-serif;font-size:5.5px;color:var(--gold)}
.bottom-nav .active{color:var(--white)}
</style>
</head>
<body>

<header class="site-header">
  <div class="brand"><span class="brand-mark"></span>HARBOR BOLTS</div>
  <nav class="main-nav">
    <span class="active">HOME</span><span>ABOUT US</span><span>PRODUCTS</span><span>CONTACT US</span>
  </nav>
</header>

<section class="hero">
  <div class="hero-photo" role="img" aria-label="Polished brass knob lock with key"></div>
  <div class="tag" style="left:256px;top:135px">DOLOR SIT ET</div>
  <div class="tag" style="left:137px;top:181px">LOREM IPSUM</div>
  <h1 class="hero-title"><span class="l1">LOREM IPSUM</span><span class="l2">DOLOR SIT AMET</span></h1>
  <ul class="hero-points">
    <li>CONSECTETUR ADIPISCING ELIT. NULLA</li>
    <li>LOBORTIS CONSEQUAT MAURIS, EGET ELEIFEND</li>
    <li>NUNC VIVERRA VIVERRA. UT AC RISUS ODIO</li>
  </ul>
  <div class="btn-light">LEARN MORE</div>
  <div class="slider-tabs"><span class="on">1</span><span>2</span><span>3</span><span>4</span><span>5</span></div>
</section>

<article class="card card-photo" style="left:91px;width:158px">
  <div class="img" role="img" aria-label="Black combination key-safe padlock" style="background:linear-gradient(#9a9a9a 0%,#3a3a3a 35%,#151515 100%)"></div>
  <div class="card-frame"></div>
  <div class="card-label">CONSEQUAT<small>MAURIS</small></div>
</article>

<article class="card card-promo">
  <div class="card-frame"></div>
  <h2>LOREM IPSUM DOLOR</h2>
  <p>Amet, consectetur adipiscing elit. Nulla lobortis consequat mauris, eget eleifend nunc viverra viverra. Ut ac risus odio. Aliquam pretium purus sed nulla feugiat blandit. Cras vel libero ut lacus eleifend tempor.</p>
  <div class="btn-dark">LEARN MORE</div>
  <div class="faint">DUIS NEC AUGUE EGET<small>VESTIBULUM ET SAPIEN</small></div>
</article>

<article class="card card-photo" style="left:507px;width:158px">
  <div class="img" role="img" aria-label="Laminated steel padlock with blue base and keys" style="background:linear-gradient(#d8d8d8 0%,#9aa5b0 55%,#2b3f9a 100%)"></div>
  <div class="card-frame"></div>
  <div class="card-label">CONSEQUAT<small>MAURIS</small></div>
</article>

<div class="divider"></div>
<h2 class="section-title">MORE FROM HARBOR BOLTS</h2>

<article class="news" style="left:91px">
  <div class="img" role="img" aria-label="Red wooden front door secured with a brass padlock" style="background:linear-gradient(135deg,#7a3a22,#4a2315 60%,#8a5a3a)"></div>
  <h3>LOREM IPSUM DOLOR</h3>
  <p>Amet, consectetur adipiscing elit. Nulla lobortis consequat mauris, eget eleifend nunc viverra viverra. Ut ac risus odio. Aliquam pretium purus sed nulla feugiat blandit.</p>
  <a>Watch Video</a>
</article>
<article class="news" style="left:288px">
  <div class="img" role="img" aria-label="Close-up of a key inserted into a cylinder lock" style="background:radial-gradient(circle at 55% 45%,#f1e4c8,#9c8466 55%,#2f3a40)"></div>
  <h3>LOREM IPSUM DOLOR</h3>
  <p>Amet, consectetur adipiscing elit. Nulla lobortis consequat mauris, eget eleifend nunc viverra viverra. Ut ac risus odio. Aliquam pretium purus sed nulla feugiat blandit.</p>
  <a>Read More</a>
</article>
<article class="news" style="left:485px">
  <div class="img" role="img" aria-label="Row of grey lockers with small brass padlocks" style="background:linear-gradient(90deg,#6d6c6a,#c9c6c1 45%,#9b9893 70%,#d6d3ce)"></div>
  <h3>LOREM IPSUM DOLOR</h3>
  <p>Amet, consectetur adipiscing elit. Nulla lobortis consequat mauris, eget eleifend nunc viverra viverra. Ut ac risus odio. Aliquam pretium purus sed nulla feugiat blandit.</p>
  <a>Read More</a>
</article>

<footer class="site-footer">
  <div class="f-col" style="left:91px"><h4>LOREM</h4><ul><li>Amet, consectetur</li><li>Adipiscing elit.</li><li>Nulla lobortis</li><li class="hl">Consequat mauris,</li><li>Eget eleifend nunc</li><li>Viverra viverra. Ut</li><li>Ac risus odio.</li><li>Aliquam pretium</li><li>Purus sed nulla</li><li>Feugiat blandit.</li></ul></div>
  <div class="f-col" style="left:194px"><h4>INTEGER EGET</h4><ul><li>Amet, consectetur</li><li>Adipiscing elit. Nulla</li><li>Lobortis Consequat mauris,</li><li>Eget eleifend nunc Viverra</li><li>Viverra. Ut Ac risus odio.</li><li>Aliquam pretium Purus sed</li><li>Nulla Feugiat blandit. Cras</li><li>Vel libero Ut lacus</li><li>Eleifend tempor.</li></ul></div>
  <div class="f-col" style="left:322px"><h4>LOREM</h4><ul><li>Amet, consectetur</li><li>Adipiscing elit.</li><li>Nulla lobortis</li><li>Consequat mauris,</li><li>Eget eleifend nunc</li><li>Viverra viverra. Ut</li><li>Ac risus odio.</li><li>Aliquam pretium</li><li>Purus sed nulla</li><li>Feugiat blandit.</li></ul></div>
  <div class="f-col" style="left:426px"><h4>INTEGER EGET</h4><ul><li>Amet, consectetur</li><li>Adipiscing elit. Nulla</li><li>Lobortis Consequat mauris,</li><li>Eget eleifend nunc Viverra</li><li>Viverra. Ut Ac risus odio.</li><li>Aliquam pretium Purus sed</li><li>Nulla Feugiat blandit. Cras</li><li>Vel libero Ut lacus</li><li>Eleifend tempor.</li></ul></div>
  <div class="f-col" style="left:558px">
    <h4>CONNECT WITH US</h4>
    <div class="social"><span></span><span></span><span></span><span></span></div>
    <h4 class="gap">CALL US</h4>
    <div class="f-info">Mon - Sat, 8am - 8pm<br>0 (000) 000-0000</div>
    <h4 class="gap">EMAIL US</h4>
    <div class="f-info">info@harborbolts.com</div>
  </div>
  <div class="bottom-bar">
    <nav class="bottom-nav"><span class="active">HOME</span><span>ABOUT US</span><span>PRODUCTS</span><span>CONTACT US</span></nav>
    <span>©2014 Harbor Bolts. All rights reserved.</span>
  </div>
</footer>

</body>
</html>
```